Website design for a personal and professional coaching firm

We need a website design of at least 5 pages for a personal and professional life and leadership Coaching and Life Services Firm. Main Interest: life, relationships and career.
Family, personal development, professional development. Companies and corporations
CHK OUT FACEBOOK PAGE: OREMBY PATH HOUSE Coaching and Life Services
Target Market(s)
Our Target Audience:
25 to 55 year old men and women living in city, suburbs, and some rural areas. Income from 50k and above. Young professionals, middle of career, college degree. Company, corporate, government, human resources sensitive industries.
Industry/Entity Type
Life Coaching
Number of Pages Required
5+ page
Requirements
Must have
- #1 - relevance/in touch
- #2 - creativity
- #3 - connection with them
Should not have
- the least amount of scrolling the better. Simple, clean and user friendly website not loaded down with a ton of reading

```html
<!DOCTYPE html>
<html lang="en">
<head>
<meta charset="utf-8">
<title>OREMBY PATH HOUSE</title>
<link href="https://fonts.googleapis.com/css2?family=Poppins:wght@300;400;600;700&family=Noto+Serif:wght@700&family=Lato:wght@300;400&family=Roboto:wght@400&display=swap" rel="stylesheet">
<style>
:root{
  --topbar:#f5f5f5;
  --line:#e2e2e2;
  --muted:#8a8a8a;
  --ink:#3a3a3a;
  --brand:#2a4a8c;
  --accent:#c8d42a;
  --nav:#3b3a50;
  --nav-dark:#2c2b3a;
  --hero-a:#1d2347;
  --hero-b:#2b3a9a;
  --hero-c:#2a2a3c;
  --link:#1d8bd6;
}
*{margin:0;padding:0;box-sizing:border-box}
html,body{width:1093px;height:1200px;overflow:hidden;background:#fff}
body{position:relative;font-family:'Poppins',sans-serif;color:var(--ink)}
.topbar{position:absolute;left:0;top:0;width:1093px;height:40px;background:var(--topbar)}
.topbar a{position:absolute;top:0;height:40px;line-height:38px;font-size:10px;color:var(--muted);text-decoration:none}
.topbar .sep{position:absolute;top:0;width:1px;height:40px;background:var(--line)}
.social{position:absolute;left:900px;top:15px;display:flex;gap:17px}
.social span{width:9px;height:9px;border-radius:50%;border:1.3px solid var(--muted)}
.header{position:absolute;left:0;top:40px;width:1093px;height:104px}
.brand{position:absolute;left:78px;top:36px;display:flex;align-items:center;gap:8px;font-family:'Poppins',sans-serif;font-weight:600;font-size:17px;color:var(--brand);letter-spacing:.5px}
.brand i{width:14px;height:14px;border-radius:50%;background:var(--brand);display:block}
.info{position:absolute;top:35px;font-size:9.5px;line-height:19px;color:#6a6a6a;text-transform:uppercase}
.info svg{position:absolute;left:-34px;top:3px}
.hero{position:absolute;left:0;top:144px;width:1093px;height:694px;background:linear-gradient(100deg,var(--hero-a) 0%,var(--hero-b) 35%,#27327a 60%,var(--hero-c) 100%)}
.nav{position:absolute;left:80px;top:0;width:773px;height:52px;background:var(--nav);display:flex;align-items:center;padding-left:32px;gap:31px}
.nav a{font-family:'Roboto',sans-serif;font-size:18px;color:#fff;text-decoration:none}
.nav a.active{color:var(--accent)}
.appoint{position:absolute;left:853px;top:0;width:178px;height:52px;background:var(--nav-dark);color:#fff;font-size:11px;font-weight:700;text-align:center;line-height:54px}
.hero-copy{position:absolute;left:73px;top:255px;color:#fff}
.kicker{font-size:11px;font-weight:700;letter-spacing:-.2px}
.hero-copy h1{font-family:'Noto Serif',serif;font-size:45px;line-height:57px;margin-top:14px;font-weight:700}
.cta{display:inline-block;margin-top:18px;color:var(--accent);font-size:13px;font-weight:700;padding-bottom:2px;border-bottom:2px solid var(--accent)}
.welcome{position:absolute;left:0;top:875px;width:1093px;text-align:center;font-family:'Lato',sans-serif;font-weight:300;font-size:38px;color:#333}
.intro{position:absolute;left:78px;top:958px;width:935px;font-family:'Lato',sans-serif;font-size:14.5px;line-height:24px;color:#444}
.materials{position:absolute;left:0;top:1180px;width:1093px;text-align:center;font-family:'Lato',sans-serif;font-size:18.5px;color:var(--link)}
</style>
</head>
<body>
<div class="topbar">
  <a style="left:78px">Terms &amp; Conditions</a>
  <span class="sep" style="left:189px"></span>
  <a style="left:207px">Privacy Policy</a>
  <span class="sep" style="left:290px"></span>
  <a style="left:307px">Membership</a>
  <a style="left:789px">Login / Register</a>
  <span class="sep" style="left:881px"></span>
  <div class="social"><span></span><span></span><span></span><span></span><span></span></div>
</div>

<header class="header">
  <div class="brand"><i></i>OREMBY PATH HOUSE</div>
  <div class="info" style="left:480px">
    <svg width="18" height="26" viewBox="0 0 18 26" fill="none" stroke="#c8d42a" stroke-width="1.6"><path d="M9 25C9 25 1.5 15 1.5 9.5a7.5 7.5 0 0 1 15 0C16.5 15 9 25 9 25z"/><circle cx="9" cy="9.5" r="3"/></svg>
    Halvern , 14 Millrow,<br>Creston, Australia
  </div>
  <div class="info" style="left:677px">
    <svg width="26" height="26" viewBox="0 0 26 26" fill="none" stroke="#c8d42a" stroke-width="1.6" style="left:-37px"><circle cx="13" cy="13" r="11.5"/><path d="M13 6v7l5 3"/></svg>
    Mon-Fri : 9:00 am to 7:00 pm<br>Sunday : Closed
  </div>
  <div class="info" style="left:891px">
    <svg width="26" height="26" viewBox="0 0 26 26" fill="none" stroke="#c8d42a" stroke-width="1.6" style="left:-38px"><path d="M6 2l4 6-2.5 2.5c1.5 3.5 4.5 6.5 8 8L18 16l6 4-3 4C11 24 2 15 2 5z"/></svg>
    (+01) 555 014 2287<br>Hello@orembypath.com
  </div>
</header>

<section class="hero" role="img" aria-label="Smiling coach in a suit speaking on a stage lit in deep blue">
  <nav class="nav">
    <a class="active">Home</a><a>About Us</a><a>Services</a><a>Blog</a><a>Contact Us</a>
  </nav>
  <div class="appoint">APPOINTMENT</div>
  <div class="hero-copy">
    <div class="kicker">I WILL TELL YOU HOW TO</div>
    <h1>Restart your career<br>to be more successful</h1>
    <span class="cta">Tell Me How</span>
  </div>
</section>

<h2 class="welcome">Welcome to OREMBY PATH HOUSE</h2>
<p class="intro">I would like for you to get very creative here. The home page coaching sites I like are not overwhelmed with material and in depth content. I would like it to set a tone for the rest of the sight. Pics of me and Dana. Have our bio on the about page with possibility of a different pic there. Something that reflects that we are about you. Colors that grab people. Maybe one of our videos on the home page. i would like for you to pick out the best videos on our social page we did and use through the sight or in places you think they fit. It may be a good place for some of the questions to appear that is on the back of the brochure. We need to push the: Call now for a Free Coaching Consult! (in person, phone or virtually)<br>555-262-0140 (Ashford)<br>555-770-0192 (Linwood)<br>555-417-0173 (Brookvale)</p>
<p class="materials">Not sure how to word this but Free Life, Relationship and Career Materials:</p>
</body>
</html>
```